Design mobile friendly real estate and property management company landing page

Design a clean, crisp modern looking landing page that is mobile-friendly (must resize, preferably using bootstrap framework). Landing page will consist of heading with login area, company info, body consists of company description and services, a list of available rental properties with photos, and a footer with additional links and info. Working on updating with text for text areas marked A, B, and C on the layout pdf, but in meantime, lorem ipsum is fine. I can connect events to most buttons, etc. Just need the bootstrap and html functionality set up. Previous company website (which should not be relied upon) is www.qlbt.net This is somewhat of a template for a start, but looking for a more professional and modern design for the new website. But this gives an idea of the content and what needs to be displayed, and how.

Target Market(s)

Clients looking for a property management company that is efficient and well-organized.

Industry/Entity Type

Property Management

Coding

Coded - Design and coding required

Number of Pages Required

1 page

Font styles to use
Sans Serif

Colors
0355a3

Requirements
Must have
• Resize for the screen using bootstrap.
• Navigation that collapses for mobile devices
• Large text boxes and good solid spacing around all elements.
Nice to have
• for property images it would be nice if they can be swiped on touch enabled devices (to the next or previous image). And have navigation that can be clicked to next or previous images.
• Would be nice if a captcha verification was included on contact form.
Should not have
• Fancy or eccentric art

```html
<!DOCTYPE html>
<html lang="en">
<head>
<meta charset="utf-8">
<title>Harbor Realty Services</title>
<link rel="stylesheet" href="https://fonts.googleapis.com/css2?family=Open+Sans:wght@400;600;700&family=Lato:wght@400;700&display=swap">
<style>
:root{
  --navy:#152039;
  --navy-2:#1b2a48;
  --blue:#0355a3;
  --blue-nav:#0a5cb8;
  --sky:#1aa3e8;
  --orange:#e8902e;
  --field:#fdbf78;
  --grey-band:#eeeeee;
  --text:#333;
  --line:#e2e2e2;
}
*{box-sizing:border-box;margin:0;padding:0}
html,body{width:746px;height:1200px;overflow:hidden;background:#fff}
body{position:relative;font-family:"Open Sans",Arial,sans-serif;color:var(--text)}
.abs{position:absolute}

/* header */
.site-header{left:0;top:0;width:746px;height:58px;background:var(--navy)}
.brand{left:62px;top:21px;color:#fff;font-family:"Open Sans",Arial,sans-serif;font-size:14px;font-weight:600;line-height:16px;display:flex;align-items:center;gap:7px}
.brand i{display:block;width:9px;height:9px;background:#fff}
.search-field{top:20px;height:20px;background:var(--navy-2);color:#9aa6bd;font-size:7.5px;padding:5px 8px;border:1px solid #24345a}
.kw{left:331px;width:146px}
.mode{left:481px;width:102px}
.mode svg{position:absolute;right:7px;top:7px}
.search-btn{left:589px;top:20px;width:24px;height:20px;background:var(--blue-nav);display:flex;align-items:center;justify-content:center}
.login{left:618px;top:20px;width:67px;height:20px;background:var(--orange);color:#fff;font-size:8px;font-weight:600;text-align:center;line-height:20px}

.main-nav{left:0;top:58px;width:746px;height:28px;background:var(--blue-nav)}
.main-nav a{position:absolute;top:0;height:28px;line-height:28px;color:#fff;font-size:8px;font-weight:600;text-decoration:none}
.main-nav .active{background:var(--sky);left:62px;width:65px;text-align:center}

/* hero */
.hero{left:0;top:86px;width:746px;height:325px;background:radial-gradient(ellipse at 45% 60%,#3a4a66 0%,#1d2a44 45%,#0f1a2e 100%)}
.hero-copy{left:62px;top:172px;width:316px;color:#fff}
.hero-copy h1{font-size:16px;font-weight:600}
.hero-copy h2{font-size:9.5px;font-weight:600;margin-top:3px}
.hero-copy p{font-size:7px;line-height:10.5px;margin-top:10px;color:#e4e8ef}
.badge{top:310px;height:20px}
.dots{left:362px;top:392px;display:flex;gap:3px}
.dots i{width:4px;height:4px;border-radius:50%;background:#ccc;display:block}
.dots i:first-child{background:var(--orange)}

.contact{left:432px;top:134px;width:253px;height:277px;background:var(--orange);border-top:3px solid var(--blue-nav)}
.contact h3{position:absolute;top:14px;width:100%;text-align:center;font-size:17px;font-weight:600;color:#2a2a2a}
.field{position:absolute;left:20px;width:214px;background:var(--field);font-size:7px;color:#8a6a45;padding:7px 12px}
.send{position:absolute;left:20px;top:228px;width:214px;height:34px;background:var(--blue-nav);color:#fff;font-size:12px;font-weight:600;text-align:center;line-height:34px;border:1px solid #fff}

/* services */
.services{left:0;top:411px;width:746px;height:253px;background:var(--grey-band)}
.section-title{width:746px;left:0;text-align:center;font-size:15px;font-weight:600;color:#2a2a2a}
.divider{left:319px;width:108px;height:4px}
.service-card{top:490px;width:304px;height:130px;background:#fff}
.service-card h4{position:absolute;left:16px;top:14px;font-size:8.5px;font-weight:600;color:#222}
.service-card p{position:absolute;left:99px;top:38px;width:190px;font-size:7px;line-height:10px;color:#888}
.service-card .icon{position:absolute;left:32px;top:42px}
.read-more{position:absolute;left:99px;top:98px;width:57px;height:17px;background:var(--blue);color:#fff;font-size:7px;font-weight:600;text-align:center;line-height:17px}

/* listings */
.list-heading{left:62px;font-size:11.5px;font-weight:600;color:#222}
.view-all{left:642px;width:43px;height:14px;background:var(--blue);color:#fff;font-size:5.5px;text-align:center;line-height:14px}
.photo{left:62px;width:112px;height:111px;border:2px solid #e6e6e6}
.listing{left:191px;width:494px;height:112px;border:1px solid var(--line);font-family:"Lato","Open Sans",sans-serif}
.listing .top{position:absolute;top:9px;left:16px;right:0;font-size:10.5px;color:var(--blue);display:flex;align-items:center}
.listing .top span{display:flex;align-items:center;gap:6px}
.specs{position:absolute;top:38px;font-size:7px;line-height:15.5px;color:#333}
.specs .k{display:inline-block;width:58px}
.specs .d{display:inline-block;width:11px}
.vline{position:absolute;top:36px;width:1px;height:63px;background:var(--line)}
.desc{position:absolute;left:328px;top:38px;width:150px;font-size:6.3px;line-height:10px;color:#333}

/* footer */
.site-footer{left:0;top:1100px;width:746px;height:100px;background:var(--navy)}
.foot-links{left:62px;top:41px;font-size:6.3px;color:#c6ccd8}
.foot-links span{margin:0 5px}
.copy{left:62px;top:56px;font-size:7px;color:#c6ccd8}
.social{top:33px;width:23px;height:23px;border-radius:50%;background:var(--navy-2);display:flex;align-items:center;justify-content:center}
</style>
</head>
<body>

<header class="abs site-header">
  <div class="abs brand"><i></i>Harbor Realty Services</div>
  <div class="abs search-field kw">Key Word</div>
  <div class="abs search-field mode">For Rent
    <svg width="6" height="4" viewBox="0 0 6 4"><path d="M0 0l3 3 3-3" stroke="#9aa6bd" fill="none"/></svg>
  </div>
  <div class="abs search-btn"><svg width="11" height="11" viewBox="0 0 12 12"><circle cx="5" cy="5" r="3.8" stroke="#fff" stroke-width="1.6" fill="none"/><path d="M8 8l3 3" stroke="#fff" stroke-width="1.8"/></svg></div>
  <div class="abs login">LOGIN</div>
</header>

<nav class="abs main-nav">
  <a class="active" href="#">Home</a>
  <a href="#" style="left:146px">For Rent</a>
  <a href="#" style="left:211px">For Sale</a>
  <a href="#" style="left:274px">Property Management</a>
  <a href="#" style="left:395px">Real Estate</a>
  <a href="#" style="left:471px">About</a>
</nav>

<section class="abs hero" role="img" aria-label="Blurred photo of a businessman's hands at a desk"></section>
<div class="abs hero-copy">
  <h1>Who We Are?</h1>
  <h2>Welcome to Tidewell Realty &amp; Management</h2>
  <p>We are a locally owned and operated San Diego Property Management company. Serving all areas of San Diego County, we provide personal, reliable property management services for all types of residential property.</p>
  <p>Please give us a call anytime at (555) 204-3187 to discuss your property management needs, or fill out our proposal request form and we will be in touch with you promptly.</p>
</div>
<div class="abs badge" style="left:62px;width:55px;background:#0b5c8f;border-radius:2px"></div>
<div class="abs badge" style="left:120px;width:42px;background:#1c3350;border-radius:2px"></div>
<div class="abs badge" style="left:170px;width:35px;background:#fff"></div>
<div class="abs badge" style="left:222px;width:22px;border:2px solid #fff;border-radius:2px"></div>
<div class="abs dots"><i></i><i></i><i></i></div>

<form class="abs contact">
  <h3>CONTACT US</h3>
  <div class="field" style="top:43px;height:23px">Name</div>
  <div class="field" style="top:73px;height:24px">Email</div>
  <div class="field" style="top:103px;height:23px">Phone</div>
  <div class="field" style="top:133px;height:24px">Subject</div>
  <div class="field" style="top:164px;height:49px">Comment</div>
  <div class="send">SEND</div>
</form>

<section class="abs services"></section>
<div class="abs section-title" style="top:441px">OUR SERVICES</div>
<svg class="abs divider" style="top:462px" viewBox="0 0 108 4"><path d="M0 2h50M58 2h50" stroke="#333" stroke-width=".8"/><circle cx="54" cy="2" r="1.8" fill="#152039"/></svg>

<article class="abs service-card" style="left:62px">
  <h4>PROPERTY MANAGEMENT SERVICES</h4>
  <svg class="icon" width="46" height="44" viewBox="0 0 46 44"><path d="M23 2L2 22h6v20h11V30h8v12h11V22h6z" fill="#b8b8b8"/></svg>
  <p>Lorem ipsum dolor sit amet, consectetur adipiscing elit. Sed auctor massa ut mi accumsan, id porta tortor maximus. Mauris accumsan erat et metus dapibus pellentesque.sce nisi nibh, porta in felis et, commodo egestas magna. Nullam nisl massa.</p>
  <div class="read-more">Read More</div>
</article>
<article class="abs service-card" style="left:382px">
  <h4>REALESTATE SERVICES</h4>
  <svg class="icon" width="56" height="42" viewBox="0 0 56 42"><rect x="2" y="2" width="22" height="40" fill="#b8b8b8"/><g fill="#fff"><rect x="6" y="7" width="4" height="4"/><rect x="12" y="7" width="4" height="4"/><rect x="6" y="15" width="4" height="4"/><rect x="12" y="15" width="4" height="4"/><rect x="6" y="23" width="4" height="4"/><rect x="12" y="23" width="4" height="4"/></g><path d="M30 22l8-8h10l6 6-14 14z" fill="none" stroke="#b8b8b8" stroke-width="2"/></svg>
  <p>Lorem ipsum dolor sit amet, consectetur adipiscing elit. Sed auctor massa ut mi accumsan, id porta tortor maximus. Mauris accumsan erat et metus dapibus pellentesque.sce nisi nibh, porta in felis et, commodo egestas magna. Nullam nisl massa.</p>
  <div class="read-more">Read More</div>
</article>

<div class="abs section-title" style="top:686px">FEATURED LISTINGS</div>
<svg class="abs divider" style="top:708px" viewBox="0 0 108 4"><path d="M0 2h50M58 2h50" stroke="#333" stroke-width=".8"/><circle cx="54" cy="2" r="1.8" fill="#152039"/></svg>

<div class="abs list-heading" style="top:735px">FOR RENT</div>
<div class="abs view-all" style="top:733px">VIEW ALL</div>
<div class="abs photo" style="top:762px;background:linear-gradient(180deg,#7d9cc4 0%,#a7b6c6 45%,#6f6a63 62%,#4e7d2f 80%,#5d9a35 100%)" role="img" aria-label="Photo of a two-storey suburban house with a lawn"></div>
<div class="abs listing" style="top:762px">
  <div class="top">
    <span style="width:212px"><svg width="7" height="10" viewBox="0 0 7 10"><path d="M3.5 0A3.5 3.5 0 0 0 0 3.5C0 6 3.5 10 3.5 10S7 6 7 3.5A3.5 3.5 0 0 0 3.5 0z" fill="#0355a3"/><circle cx="3.5" cy="3.5" r="1.3" fill="#fff"/></svg>4352 Birch Ave San Diego, CA 92104</span>
    <span style="width:89px"><svg width="13" height="8" viewBox="0 0 13 8"><path d="M1 0v8M1 5h11v3M4 3h8v2" stroke="#0355a3" stroke-width="1.3" fill="none"/></svg>2 Bedroom</span>
    <span><svg width="11" height="10" viewBox="0 0 11 10"><path d="M2 9V1h2M0 5h11v2a2 2 0 0 1-2 2H3" stroke="#0355a3" stroke-width="1.2" fill="none"/></svg>1 Bath Condo</span>
  </div>
  <div class="specs" style="left:16px"><div><span class="k">Rent:</span><span class="d">-</span>$1,600.00</div><div><span class="k">Available:</span><span class="d">-</span>6/1/2016</div><div><span class="k">Sqft:</span><span class="d">-</span>675</div><div><span class="k">Lease:</span><span class="d">-</span>12 Months</div></div>
  <div class="vline" style="left:138px"></div>
  <div class="specs" style="left:156px"><div><span class="k">Community:</span><span class="d">-</span>North Park</div><div><span class="k">Parking:</span><span class="d">-</span>2 assigned spaces off-s...</div><div><span class="k">Pets:</span><span class="d">-</span>Inquire</div><div><span class="k">Laundry:</span><span class="d">-</span>On-Site</div></div>
  <div class="vline" style="left:318px"></div>
  <div class="desc">Highly upgraded 2BR/1BA condo in gated North Park community. Unit features hard-wood flooring, granite counters in kitchen and bathroom, appliances included. Two assigned off-street parking spaces. Must have excellent rental history, sorry, No ...</div>
</div>

<div class="abs list-heading" style="top:898px">FOR SALE</div>
<div class="abs view-all" style="top:896px">VIEW ALL</div>
<div class="abs photo" style="top:926px;background:linear-gradient(180deg,#4d6a9a 0%,#6f7fa0 35%,#8a6a55 62%,#3f5a74 82%,#3fa3b8 100%)" role="img" aria-label="Photo of a modern house at dusk with a pool"></div>
<div class="abs listing" style="top:925px">
  <div class="top">
    <span style="width:212px"><svg width="7" height="10" viewBox="0 0 7 10"><path d="M3.5 0A3.5 3.5 0 0 0 0 3.5C0 6 3.5 10 3.5 10S7 6 7 3.5A3.5 3.5 0 0 0 3.5 0z" fill="#0355a3"/><circle cx="3.5" cy="3.5" r="1.3" fill="#fff"/></svg>1354 Lorem isps San Diego, CA 92104</span>
    <span style="width:89px"><svg width="13" height="8" viewBox="0 0 13 8"><path d="M1 0v8M1 5h11v3M4 3h8v2" stroke="#0355a3" stroke-width="1.3" fill="none"/></svg>2 Bedroom</span>
    <span><svg width="11" height="10" viewBox="0 0 11 10"><path d="M2 9V1h2M0 5h11v2a2 2 0 0 1-2 2H3" stroke="#0355a3" stroke-width="1.2" fill="none"/></svg>1 Bath Condo</span>
  </div>
  <div class="specs" style="left:16px"><div><span class="k">Rent:</span><span class="d">-</span>$1,600.00</div><div><span class="k">Available:</span><span class="d">-</span>6/1/2016</div><div><span class="k">Sqft:</span><span class="d">-</span>675</div><div><span class="k">Lease:</span><span class="d">-</span>12 Months</div></div>
  <div class="vline" style="left:138px"></div>
  <div class="specs" style="left:156px"><div><span class="k">Community:</span><span class="d">-</span>North Park</div><div><span class="k">Parking:</span><span class="d">-</span>2 assigned spaces off-s...</div><div><span class="k">Pets:</span><span class="d">-</span>Inquire</div><div><span class="k">Laundry:</span><span class="d">-</span>On-Site</div></div>
  <div class="vline" style="left:318px"></div>
  <div class="desc">Highly upgraded 2BR/1BA condo in gated North Park community. Unit features hard-wood flooring, granite counters in kitchen and bathroom, appliances included. Two assigned off-street parking spaces. Must have excellent rental history, sorry, No ...</div>
</div>

<footer class="abs site-footer">
  <div class="abs foot-links">Privacy Policy<span>|</span>Info<span>|</span>Contact<span>|</span>2870 Laurel Ave, San Diego, CA 92107</div>
  <div class="abs copy">©2016 Tidewell Realty &amp; Management. All Rights Reserved.</div>
  <div class="abs social" style="left:605px;background:#1877f2" aria-label="Email">
    <svg width="11" height="8" viewBox="0 0 11 8"><rect x=".5" y=".5" width="10" height="7" fill="none" stroke="#fff"/><path d="M.5 .5l5 4 5-4" fill="none" stroke="#fff"/></svg>
  </div>
  <div class="abs social" style="left:634px" aria-label="Phone">
    <svg width="10" height="10" viewBox="0 0 10 10"><path d="M2 .5l2 2-1 1.5a6 6 0 0 0 3 3L7.5 6l2 2-1.5 1.5C4 9 1 6 .5 2z" fill="#fff"/></svg>
  </div>
  <div class="abs social" style="left:662px" aria-label="Share">
    <svg width="10" height="10" viewBox="0 0 10 10"><circle cx="2" cy="5" r="1.6" fill="#fff"/><circle cx="8" cy="2" r="1.6" fill="#fff"/><circle cx="8" cy="8" r="1.6" fill="#fff"/><path d="M2 5l6-3M2 5l6 3" stroke="#fff" stroke-width=".9"/></svg>
  </div>
</footer>

</body>
</html>
```